Design Chinese text on the PSD banner template

Add Chinese text on the PSD banner template.
-delete all the current text on the template
-the design of the text must suite the template, prefer high end, luxury, gold metal effect.

main text:
批盘 90%

secondary text:
-真人 -电子 -捕鱼 -体育 -棋牌 -彩票
多达1200++种游戏

Banner PSD template download link:
https://qv.zx/t-RAPlWoUbtz

(the meaning of those Chinese text is:

Wholesale Game Credit 90%

-live game -slot game -fishing game -sports game -poker game -lottery game
more than 1200++ games )

```html
<!DOCTYPE html>
<html lang="zh-CN">
<head>
<meta charset="utf-8">
<title>批盘 90% 横幅</title>
<link rel="stylesheet" href="https://fonts.googleapis.com/css2?family=Noto+Sans+SC:wght@700;900&display=swap">
<style>
  :root {
    --bg-deep: #0d0703;
    --bg-brown: #3a2308;
    --bg-glow: #a97a1c;
    --gold-light: #fff6a8;
    --gold-mid: #f5cc2e;
    --gold-deep: #b9790c;
    --gold-dark: #5a3504;
    --shadow-brown: #2a1702;
    --star: #f7e23a;
  }
  html, body {
    margin: 0;
    padding: 0;
    width: 1017px;
    height: 1200px;
    overflow: hidden;
    background: var(--bg-deep);
  }
  .banner {
    position: relative;
    width: 1017px;
    height: 1200px;
    overflow: hidden;
    font-family: "Noto Sans SC", sans-serif;
  }
  .spotlight-backdrop {
    position: absolute;
    inset: 0;
    background:
      radial-gradient(ellipse 80% 65% at 50% 5%, var(--bg-glow) 0%, #7a5514 30%, var(--bg-brown) 62%, var(--bg-deep) 100%);
  }
  .stars {
    position: absolute;
    top: 100px;
    left: 0;
    width: 100%;
    display: flex;
    justify-content: center;
    gap: 36px;
  }
  .stars svg { width: 40px; height: 40px; }
  .headline {
    position: absolute;
    top: 548px;
    left: 0;
    width: 100%;
    margin: 0;
    text-align: center;
    font-weight: 700;
    font-size: 204px;
    line-height: 1;
    letter-spacing: 2px;
    white-space: nowrap;
    background: linear-gradient(180deg, var(--gold-light) 10%, var(--gold-mid) 45%, var(--gold-deep) 75%, #e9b73a 100%);
    -webkit-background-clip: text;
    background-clip: text;
    color: transparent;
    filter: drop-shadow(0 2px 0 var(--gold-dark)) drop-shadow(3px 5px 0 var(--shadow-brown)) drop-shadow(0 0 10px rgba(0,0,0,.6));
  }
  .underline-bar {
    position: absolute;
    top: 787px;
    left: 60px;
    width: 893px;
    height: 30px;
    border-radius: 4px;
    background: linear-gradient(180deg, var(--gold-light) 0%, var(--gold-mid) 40%, var(--gold-deep) 75%, var(--gold-dark) 100%);
    box-shadow: 0 4px 6px rgba(0,0,0,.7);
  }
  .sub {
    position: absolute;
    left: 0;
    width: 100%;
    margin: 0;
    text-align: center;
    font-weight: 700;
    line-height: 1;
    white-space: nowrap;
    background: linear-gradient(180deg, var(--gold-light) 0%, var(--gold-mid) 50%, var(--gold-deep) 100%);
    -webkit-background-clip: text;
    background-clip: text;
    color: transparent;
    filter: drop-shadow(2px 3px 0 var(--shadow-brown));
  }
  .sub-categories { top: 846px; font-size: 57px; letter-spacing: -1px; }
  .sub-count { top: 918px; font-size: 56px; }
</style>
</head>
<body>
<main class="banner">
  <div class="spotlight-backdrop" role="img" aria-label="Golden spotlight rays shining down with glittering gold particles"></div>

  <div class="stars" aria-label="五星">
    <svg viewBox="0 0 24 24"><polygon fill="var(--star)" points="12,1 15,9 23,9 16.5,14 19,22 12,17 5,22 7.5,14 1,9 9,9"/></svg>
    <svg viewBox="0 0 24 24"><polygon fill="var(--star)" points="12,1 15,9 23,9 16.5,14 19,22 12,17 5,22 7.5,14 1,9 9,9"/></svg>
    <svg viewBox="0 0 24 24"><polygon fill="var(--star)" points="12,1 15,9 23,9 16.5,14 19,22 12,17 5,22 7.5,14 1,9 9,9"/></svg>
    <svg viewBox="0 0 24 24"><polygon fill="var(--star)" points="12,1 15,9 23,9 16.5,14 19,22 12,17 5,22 7.5,14 1,9 9,9"/></svg>
    <svg viewBox="0 0 24 24"><polygon fill="var(--star)" points="12,1 15,9 23,9 16.5,14 19,22 12,17 5,22 7.5,14 1,9 9,9"/></svg>
  </div>

  <h1 class="headline">批盘 90%</h1>
  <div class="underline-bar"></div>
  <p class="sub sub-categories">-真人 -电子 -捕鱼 -体育 -棋牌 -彩票</p>
  <p class="sub sub-count">多达1200++种游戏</p>
</main>
</body>
</html>
```